WPO Gel Nail Polish Collection for 15 ml bottle

We need a design for our new collection of WPO brand gel nail polish, called "SILK FOG". We are a nail salon / beauty supply distributor selling to retail nail salons in the US. Please look at the sample nail polish bottles attached for your reference. Our bottle will be white with a silver cap. Also, please look at our other project that is on HV for label design for the matching color tip swatches.

Target Market(s)

Retail Nail Salons in the US

Industry/Entity Type

Nail Salon

Colors

Designer to choose colors to be used in the design.

Requirements
Must have
• WPO logo - this needs to be changed to black color for letters WPO and matte gold for the "drop".
• PREMIUM GEL POLISH, SILK FOG, 0.5 oz (15 ml), back label wording.
• Front label wording must be clear and easy to read.
• Dimensions of label must be 1.125" x 4.0".
• Front part of label and back part of label must be spaced correctly so that they will be on opposite sides of the bottle.
Nice to have
• Color stripe possibly where the product name "SILK FOG" will appear, so that it stands out.
Should not have
• no actual pictures of SILK FOG, no overpowering graphics

```html
<!DOCTYPE html>
<html lang="en">
<head>
<meta charset="utf-8">
<title>WPO Premium Gel Polish – SILK FOG Label</title>
<link href="https://fonts.googleapis.com/css2?family=Arimo&family=Barlow:wght@400;500;600;700&display=swap" rel="stylesheet">
<style>
  :root {
    --canvas: #e6e6e6;
    --paper: #ffffff;
    --gold: #d2923a;
    --ink: #000000;
    --text: #1f1f1f;
    --red: #ee1c25;
    --label-font: "Barlow", sans-serif;
    --title-font: "Arimo", Arial, sans-serif;
  }
  * { margin: 0; padding: 0; box-sizing: border-box; }
  html, body { width: 1200px; height: 1199px; overflow: hidden; }
  body { background: var(--canvas); position: relative; font-family: var(--label-font); }

  .view-title {
    position: absolute; font-family: var(--title-font); font-size: 40px;
    color: var(--ink); transform: translateX(-50%); white-space: nowrap; line-height: 1;
  }

  .label { position: absolute; height: 311px; background: var(--paper); }
  .band { position: absolute; left: 0; right: 0; }
  .band-gold-top { top: 0; height: 20px; background: var(--gold); }
  .band-black { top: 253px; height: 29px; background: var(--ink); }
  .band-gold-bottom { top: 290px; height: 21px; background: var(--gold); }

  .front-panel { position: absolute; top: 0; width: 402px; height: 311px; }
  .brand-name {
    position: absolute; left: 0; right: 0; top: 50px; text-align: center;
    font-family: var(--label-font); font-weight: 700; font-size: 100px;
    line-height: 1; color: var(--ink);
  }
  .rule { position: absolute; left: 44px; width: 313px; top: 143px; height: 1.5px; background: var(--ink); }
  .line-type {
    position: absolute; left: 0; right: 0; top: 151px; text-align: center;
    font-size: 21px; font-weight: 500; color: var(--text); letter-spacing: 0.3px;
  }
  .shade-name {
    position: absolute; left: 0; right: 0; top: 178px; text-align: center;
    font-size: 54px; font-weight: 700; color: var(--red); line-height: 1;
  }
  .volume {
    position: absolute; left: 0; right: 0; top: 253px; height: 29px; line-height: 29px;
    text-align: center; color: var(--paper); font-size: 19px; font-weight: 500;
  }

  .back-panel { position: absolute; top: 0; width: 402px; height: 311px; }
  .back-heading {
    position: absolute; left: 0; right: 0; top: 39px; text-align: center; padding-left: 10px;
    color: var(--red); font-weight: 700; font-size: 14.5px;
  }
  .back-copy { position: absolute; font-size: 10.3px; line-height: 12.9px; color: var(--text); white-space: nowrap; }
  .back-copy h3 { font-size: 10.3px; font-weight: 700; }
  .back-copy p { font-weight: 400; }
  .back-copy .warning { color: var(--red); font-weight: 700; }
  .directions { left: 71px; top: 75px; }
  .caution { left: 68px; top: 183px; }
</style>
</head>
<body>

<div class="view-title" style="left:363px; top:187px;">Front Label</div>
<div class="view-title" style="left:846px; top:187px;">Back Label</div>
<div class="view-title" style="left:606px; top:663px;">Whole Label</div>

<section class="label" style="left:163px; top:245px; width:402px;">
  <div class="band band-gold-top"></div>
  <div class="band band-black"></div>
  <div class="band band-gold-bottom"></div>
  <div class="front-panel" style="left:0;">
    <div class="brand-name">WPO</div>
    <div class="rule"></div>
    <div class="line-type">PREMIUM GEL POLISH</div>
    <div class="shade-name">SILK FOG</div>
    <div class="volume">0.5 oz (15 ml)</div>
  </div>
</section>

<section class="label" style="left:645px; top:245px; width:402px;">
  <div class="band band-gold-top"></div>
  <div class="band band-black"></div>
  <div class="band band-gold-bottom"></div>
  <div class="back-panel" style="left:0;">
    <div class="back-heading">FOR PROFESSIONAL USE ONLY</div>
    <div class="back-copy directions">
      <h3>DIRECTIONS FOR USE:</h3>
      <p>Apply 1 coat over preferred gel polish base coat.</p>
      <p>Use magnet to create cat eye design after 2nd coat before</p>
      <p>curing with LED/UV light.</p>
      <p>Finish with preferred gel polish top coat.</p>
      <p>Must cure with LED/UV light after each coat.</p>
      <p>Approximate cure times: LED 30 seconds; UV 1-2 minutes.</p>
    </div>
    <div class="back-copy caution">
      <h3>CAUTION:</h3>
      <p class="warning">KEEP OUT OF REACH OF CHILDREN.</p>
      <p>Avoid skin contact.</p>
      <p>Discontinue use if sensitivity or irritation occurs.</p>
      <p>Avoid direct sunlight or exposure to extreme heat.</p>
    </div>
  </div>
</section>

<section class="label" style="left:51px; top:710px; width:1108px;">
  <div class="band band-gold-top"></div>
  <div class="band band-black"></div>
  <div class="band band-gold-bottom"></div>
  <div class="front-panel" style="left:145px;">
    <div class="brand-name">WPO</div>
    <div class="rule"></div>
    <div class="line-type">PREMIUM GEL POLISH</div>
    <div class="shade-name">SILK FOG</div>
    <div class="volume">0.5 oz (15 ml)</div>
  </div>
  <div class="back-panel" style="left:698px;">
    <div class="back-heading">FOR PROFESSIONAL USE ONLY</div>
    <div class="back-copy directions">
      <h3>DIRECTIONS FOR USE:</h3>
      <p>Apply 1 coat over preferred gel polish base coat.</p>
      <p>Use magnet to create cat eye design after 2nd coat before</p>
      <p>curing with LED/UV light.</p>
      <p>Finish with preferred gel polish top coat.</p>
      <p>Must cure with LED/UV light after each coat.</p>
      <p>Approximate cure times: LED 30 seconds; UV 1-2 minutes.</p>
    </div>
    <div class="back-copy caution">
      <h3>CAUTION:</h3>
      <p class="warning">KEEP OUT OF REACH OF CHILDREN.</p>
      <p>Avoid skin contact.</p>
      <p>Discontinue use if sensitivity or irritation occurs.</p>
      <p>Avoid direct sunlight or exposure to extreme heat.</p>
    </div>
  </div>
</section>

</body>
</html>
```